Quorvex.com.au - Managed online product sales programs, software platform and apps.

1. Sales & Distribution.We sell your products. On multiple websites, or to major retailers and independents, Clearance and job lots. We managed sales of products via our existing retail channels or a combination of .our channels and clients channels.
2. Software Applications. Use our platforms to manage the products, sales, tracking , customer service and more. Download our apps. Use of our platforms, like www.plindar.com , or one of our many webstores, like vornibuy.com.au . Use of our apps for product management, sales, tracking and customer service notifications
3. Marketing .Omni channel Programs Online Marketing and SEO optimisation, to maximise your exposure. Marketing - SEO and strategies to increase sales and broaden exposure.

4. Consulting. Special projects and Custom work from advise, to software development. Consulting and Review - Specialised and customised work and business intelligence to improve clients business systems.

Target Market(s)

Target customers are either:
Wholesalers, i.e. companies who own warehouses of inventory and distribute products as wholesalers.
Retailers, i.e. companies operating multiple retail stores and now want to start an online sales program.
Dropship agents, i.e. people who act as brokers, selling products on behalf of wholesalers.
Freight and transport companies who need realtime tracking of products, during delivery from pickup aat warehouse through to delicery at customer.

Industry/Entity Type

Software

Colors

Designer to choose colors to be used in the design.

Requirements
Must have
• A. Simple home page without clutter. Just an easy registration and startup.
minimal menus.
B. Use of icons to indicate each of the 4 areas of work. Namely:
1. Sales - managed sales of products via our existing retail channels or a combination of .our channels and clients channels.
2. Software - use of our platforms, like www.plindar.com , or one of our many webstores. Use of our apps for product management, sales, tracking and customer service notifications
3. Marketing - SEO and strategies to increase sales and broaden exposure.
4. Consulting and Review - Specialised and customised work and business intelligence to improve clients business systems.

C. Registration wizard to on-board a supplier in 3 easy steps, and start selling products. For example list on quilmo in 2 easy steps.

D. Use of HTML5 for graphic interface, moving icons and images for a dynamic experience.

E. Internal app-store to download our own apps.

F. Graphical explanations instead of words.

G. Real images and photos
Should not have
• Many menus.
long winded wordy explanations.

```html
<!DOCTYPE html>
<html lang="en">
<head>
<meta charset="utf-8">
<title>Quorvex</title>
<link rel="stylesheet" href="https://fonts.googleapis.com/css2?family=Carlito:wght@400;700&display=swap">
<style>
:root{
  --pink:#e8428a;
  --ink:#1a1a1a;
  --text:#333;
  --muted:#555;
  --card:#f4f4f4;
  --panel:rgba(52,52,52,.92);
  --field:#2b2b2b;
  --circle:#efefef;
}
*{margin:0;padding:0;box-sizing:border-box}
html,body{width:732px;height:1200px;overflow:hidden;background:#fff}
body{position:relative;font-family:"Carlito",Calibri,Arial,sans-serif;color:var(--text)}
.abs{position:absolute}

.site-header{left:0;top:0;width:732px;height:50px;background:linear-gradient(#fafafa,#eee)}
.brand{left:72px;top:15px;display:flex;align-items:center;gap:6px;font-weight:700;font-size:20px;letter-spacing:1px;color:var(--ink)}
.brand-mark{width:14px;height:14px;background:var(--pink)}
.main-nav{left:383px;top:19px;display:flex;gap:15px;font-size:10px;font-weight:700;color:var(--ink)}
.main-nav .active{color:var(--pink)}
.login-btn{left:585px;top:17px;width:52px;height:18px;background:var(--pink);color:#fff;font-size:9.5px;font-weight:700;display:flex;align-items:center;justify-content:center;gap:3px}
.search-btn{left:641px;top:17px;width:19px;height:18px;background:#222}

.hero{left:0;top:50px;width:732px;height:362px;background:linear-gradient(100deg,#cfd6dd 0%,#b9a596 30%,#dcdfe2 55%,#c7cdd3 80%,#e4e6e8 100%)}
.quick-reg{left:475px;top:84px;width:185px;height:274px;background:var(--panel);padding:14px 10px}
.quick-reg h2{font-weight:400;font-size:22px;color:var(--pink);line-height:1}
.quick-reg h3{font-size:12px;color:#fff;margin-bottom:10px}
.field{height:21px;background:var(--field);border:1px solid #444;color:#999;font-size:7px;padding:6px 5px;margin-bottom:8px}
.field.msg{height:66px}
.go-btn{display:inline-block;background:var(--pink);color:#fff;font-weight:700;font-size:9px;padding:8px 11px;margin-top:2px}
.slider-dots{left:345px;top:384px;display:flex;gap:3px}
.slider-dots i{width:9px;height:9px;border-radius:50%;background:#111}
.slider-dots i:first-child{background:var(--pink)}

.section-title{left:0;top:440px;width:732px;text-align:center;font-size:16px;font-weight:700;color:#333}
.sales{left:71px;top:467px;width:181px;height:208px;background:var(--pink);color:#fff;padding:12px 13px}
.sales h4{font-size:12px;margin:8px 0 6px}
.sales p{font-size:12px;line-height:16px}
.read-more{display:inline-block;background:#000;color:#fff;font-weight:700;font-size:8.5px;padding:8px 7px;margin-top:10px}
.video{left:252px;top:467px;width:409px;height:208px;background:linear-gradient(100deg,#0d1d5c 0%,#1c3f9a 40%,#3a2a5c 65%,#e0661c 90%,#f3a33a 100%)}
.play{left:428px;top:545px}

.card{top:693px;width:181px;height:145px;background:var(--card);padding:20px 13px 0;position:absolute}
.card h4{display:flex;align-items:center;gap:6px;font-size:12px;color:var(--pink);margin-bottom:12px}
.card p{font-size:8.5px;line-height:12px;color:var(--muted);height:68px}
.card .read-more{margin-top:3px}

.wizard-title{left:0;top:875px;width:732px;text-align:center;font-size:16px;line-height:18px}
.wizard-title strong{color:var(--pink)}
.step{top:939px;width:104px;text-align:center;position:absolute}
.step .bubble{width:104px;height:104px;border-radius:50%;background:var(--circle);display:flex;align-items:center;justify-content:center}
.step span{display:block;margin-top:13px;font-size:12px;font-weight:700;color:var(--pink)}
.chev{top:982px}
.next-btn{left:316px;top:1091px;width:106px;height:26px;background:#000;border-radius:5px;color:#fff;font-weight:700;font-size:12px;display:flex;align-items:center;justify-content:center}

.site-footer{left:0;top:1138px;width:732px;height:62px;background:var(--pink);color:#fff}
.site-footer small{position:absolute;left:71px;top:34px;font-size:9px}
.social{position:absolute;left:599px;top:22px;display:flex;gap:3px}
.social i{width:18px;height:18px;border-radius:50%;border:1px solid #fff}
</style>
</head>
<body>
<header class="site-header abs">
  <div class="brand abs"><span>QUORVEX</span><span class="brand-mark"></span></div>
  <nav class="main-nav abs"><span class="active">HOME</span><span>ABOUT US</span><span>CONTACT US</span></nav>
  <div class="login-btn abs"><svg width="7" height="8" viewBox="0 0 7 8"><rect x="0" y="3" width="7" height="5" fill="#fff"/><path d="M1.5 3V2a2 2 0 0 1 4 0v1" stroke="#fff" fill="none"/></svg>LOGIN</div>
  <div class="search-btn abs"><svg width="19" height="18" viewBox="0 0 19 18"><circle cx="8" cy="8" r="4" stroke="#fff" stroke-width="1.5" fill="none"/><path d="M11 11l4 4" stroke="#fff" stroke-width="1.8"/></svg></div>
</header>

<section class="hero abs" role="img" aria-label="Photo of three colleagues smiling around a desk reviewing documents"></section>
<form class="quick-reg abs">
  <h2>Quick</h2>
  <h3>Registration</h3>
  <div class="field">Name</div>
  <div class="field">E-Mail</div>
  <div class="field">Phone</div>
  <div class="field msg">Message</div>
  <span class="go-btn">GET STARTED</span>
</form>
<div class="slider-dots abs"><i></i><i></i><i></i><i></i></div>

<h2 class="section-title abs">Areas Of Work</h2>
<article class="sales abs">
  <svg width="30" height="26" viewBox="0 0 30 26"><path d="M15 1l-5 6h10z" fill="none" stroke="#fff"/><rect x="2" y="7" width="26" height="18" rx="2" fill="#fff"/><text x="15" y="20" font-size="8" text-anchor="middle" fill="#e8428a" font-family="Carlito,sans-serif">SALE</text></svg>
  <h4>Sales</h4>
  <p>Managed sales of products via our existing retail channels or a combination of .our channels and clients channels.</p>
  <span class="read-more">Read More &gt;&gt;</span>
</article>
<div class="video abs" role="img" aria-label="Video still of glowing news screens receding into a bright orange light"></div>
<svg class="play abs" width="52" height="52" viewBox="0 0 52 52"><circle cx="26" cy="26" r="24" fill="none" stroke="#fff" stroke-width="3"/><path d="M20 15l16 11-16 11z" fill="#fff"/></svg>

<article class="card" style="left:71px">
  <h4><svg width="20" height="16" viewBox="0 0 20 16"><rect x="1" y="1" width="18" height="11" fill="none" stroke="#111" stroke-width="2"/><rect x="7" y="13" width="6" height="2" fill="#111"/></svg>Software</h4>
  <p>use of our platforms, like www.plindar.com , or one of our many webstores. Use of our apps for product management, sales, tracking and customer service notifications</p>
  <span class="read-more">Read More &gt;&gt;</span>
</article>
<article class="card" style="left:276px">
  <h4><svg width="20" height="16" viewBox="0 0 20 16"><path d="M1 1v14h18" stroke="#111" fill="none" stroke-width="1.5"/><rect x="4" y="4" width="3" height="10" fill="#111"/><rect x="8" y="7" width="3" height="7" fill="#111"/><rect x="12" y="10" width="3" height="4" fill="#111"/></svg>Marketing</h4>
  <p>SEO and strategies to increase sales and broaden exposure</p>
  <span class="read-more">Read More &gt;&gt;</span>
</article>
<article class="card" style="left:480px">
  <h4><svg width="20" height="16" viewBox="0 0 20 16"><rect x="1" y="4" width="18" height="11" fill="#111"/><rect x="7" y="1" width="6" height="4" fill="none" stroke="#111" stroke-width="1.5"/><path d="M1 9h18" stroke="#fff"/></svg>Consulting and Review</h4>
  <p>Specialised and customised work and business intelligence to improve clients business systems</p>
  <span class="read-more">Read More &gt;&gt;</span>
</article>

<h2 class="wizard-title abs"><strong>Registration wizard to on-board a supplier in</strong><br>3 easy steps, and start selling products</h2>
<div class="step" style="left:110px"><div class="bubble"><svg width="36" height="32" viewBox="0 0 36 32"><path d="M3 3h5l6 20" stroke="#444" stroke-width="2.5" fill="none"/><rect x="13" y="8" width="16" height="12" transform="rotate(-15 21 14)" fill="#444"/><circle cx="16" cy="27" r="3" fill="none" stroke="#444" stroke-width="2"/></svg></div><span>Step 1</span></div>
<svg class="chev abs" style="left:256px" width="12" height="16" viewBox="0 0 12 16"><path d="M2 2l7 6-7 6" stroke="#111" stroke-width="2.5" fill="none"/></svg>
<div class="step" style="left:314px"><div class="bubble"><svg width="24" height="30" viewBox="0 0 24 30"><path d="M2 2h14l6 6v20H2z" fill="none" stroke="#444" stroke-width="2"/><path d="M6 11h12M6 15h12M6 19h12M6 23h12" stroke="#444" stroke-width="1.5"/></svg></div><span>Step 2</span></div>
<svg class="chev abs" style="left:469px" width="12" height="16" viewBox="0 0 12 16"><path d="M2 2l7 6-7 6" stroke="#111" stroke-width="2.5" fill="none"/></svg>
<div class="step" style="left:521px"><div class="bubble"><svg width="34" height="28" viewBox="0 0 34 28"><rect x="1" y="7" width="32" height="20" rx="2" fill="#444"/><rect x="12" y="2" width="10" height="6" fill="none" stroke="#444" stroke-width="2"/><path d="M1 16h32" stroke="#fff"/><rect x="8" y="13" width="4" height="6" fill="#fff"/><rect x="22" y="13" width="4" height="6" fill="#fff"/></svg></div><span>Step 3</span></div>
<div class="next-btn abs">Next</div>

<footer class="site-footer abs">
  <small>© 2014 Company Name ,All Rights Reserved</small>
  <div class="social"><i></i><i></i><i></i></div>
</footer>
</body>
</html>
```